New Business Cards For Urban Grow Store
Attention Grabber New High End Grow Store
New Business Cards For Urban Grow Store - Agriculture
Creative Brief
Bright & Fun-filled
The Hearthside Planter
Organic Specialist
4870 Pine Ridge Rd Columbia,Missouri 65203
1.877.Fe.Sprig
Bloom@TheHearthsidePlanter.example
TheHearthsidePlanter.example
Please place this on the front along the bottom please.."Custom Delveries Available "
www.TheHearthsidePlanter.example Bloom@TheHearthsidePlanter.example, 1.877.Fe.Sprig Besides the website email and phone number,Blank on back with lines to write notes.

```html
<!DOCTYPE html>
<html lang="en">
<head>
<meta charset="utf-8">
<title>The Hearthside Planter – Business Card</title>
<link href="https://fonts.googleapis.com/css2?family=Open+Sans:wght@400;600;700;800&display=swap" rel="stylesheet">
<style>
  :root {
    --page-bg: #ece9e4;
    --leaf-green: #4f8f1f;
    --leaf-green-dark: #3c7314;
    --leaf-green-light: #6aab2e;
    --icon-green: #2f5f12;
    --panel-white: #ffffff;
    --panel-shade: #eef0ec;
    --text-dark: #2c3a22;
  }
  * { box-sizing: border-box; margin: 0; padding: 0; }
  html, body {
    width: 1200px; height: 900px; overflow: hidden;
    background: var(--page-bg);
    font-family: "Open Sans", Arial, sans-serif;
  }
  .canvas {
    position: relative; width: 1200px; height: 900px;
  }
  .business-card {
    position: absolute; left: 100px; top: 165px;
    width: 1000px; height: 570px;
    border-radius: 10px;
    background: linear-gradient(180deg, var(--leaf-green-light) 0%, var(--leaf-green) 45%, var(--leaf-green-dark) 100%);
    box-shadow: 0 10px 30px rgba(0,0,0,0.18);
  }
  .brand-panel {
    position: absolute; left: 46px; top: 40px;
    width: 908px; height: 262px;
    background: linear-gradient(180deg, var(--panel-white) 70%, var(--panel-shade) 100%);
    border-radius: 46px 46px 10px 10px;
    display: flex; align-items: center; justify-content: center;
  }
  .brand-mark {
    display: flex; align-items: center; gap: 16px;
  }
  .brand-dot {
    width: 46px; height: 46px; border-radius: 50%;
    background: var(--leaf-green);
  }
  .brand-name {
    font-weight: 800; font-size: 38px; color: var(--leaf-green-dark);
    letter-spacing: 0.5px;
  }
  .title-band {
    position: absolute; left: 0; right: 0; top: 302px; height: 74px;
    display: flex; align-items: center; justify-content: center;
    color: #fff; font-size: 27px;
  }
  .title-band .company { font-weight: 700; }
  .title-band .divider { margin: 0 14px; font-weight: 400; opacity: 0.9; }
  .title-band .role { font-weight: 400; }
  .contact-panel {
    position: absolute; left: 46px; top: 376px;
    width: 908px; height: 160px;
    background: linear-gradient(180deg, var(--panel-shade) 0%, var(--panel-white) 30%);
    border-radius: 10px 10px 46px 46px;
    padding: 38px 0 0 26px;
    color: var(--text-dark); font-size: 21px; font-weight: 600;
  }
  .contact-row { display: flex; align-items: center; height: 36px; }
  .contact-item { display: inline-flex; align-items: center; gap: 7px; margin-right: 12px; }
  .contact-icon { width: 24px; height: 24px; flex: none; }
</style>
</head>
<body>
<div class="canvas">
  <div class="business-card">
    <div class="brand-panel">
      <div class="brand-mark">
        <span class="brand-dot"></span>
        <span class="brand-name">The Hearthside Planter</span>
      </div>
    </div>

    <div class="title-band">
      <span class="company">The Hearthside Planter</span>
      <span class="divider">|</span>
      <span class="role">Organic Specialist</span>
    </div>

    <div class="contact-panel">
      <div class="contact-row">
        <span class="contact-item">
          <svg class="contact-icon" viewBox="0 0 24 24" aria-hidden="true"><circle cx="12" cy="12" r="12" fill="var(--icon-green)"/><path d="M12 5a4.5 4.5 0 0 0-4.5 4.5c0 3.4 4.5 9 4.5 9s4.5-5.6 4.5-9A4.5 4.5 0 0 0 12 5zm0 6.2a1.7 1.7 0 1 1 0-3.4 1.7 1.7 0 0 1 0 3.4z" fill="#fff"/></svg>
          4870 Pine Ridge Rd Columbia,Missouri 65203
        </span>
        <span class="contact-item">
          <svg class="contact-icon" viewBox="0 0 24 24" aria-hidden="true"><circle cx="12" cy="12" r="12" fill="var(--icon-green)"/><path d="M8.6 6.2l1.8-.4 1.2 3-1.3 1a7 7 0 0 0 3.9 3.9l1-1.3 3 1.2-.4 1.8c-.2.6-.8 1-1.4.9A10.5 10.5 0 0 1 7.7 7.6c-.1-.6.3-1.2.9-1.4z" fill="#fff"/></svg>
          1.877.Fe.Sprig
        </span>
        <span class="contact-item">
          <svg class="contact-icon" viewBox="0 0 24 24" aria-hidden="true"><circle cx="12" cy="12" r="12" fill="var(--icon-green)"/><rect x="8" y="5" width="8" height="14" rx="1.5" fill="#fff"/><rect x="9.3" y="7" width="5.4" height="8.5" fill="var(--icon-green)"/></svg>
          1.877.555.0142
        </span>
      </div>
      <div class="contact-row">
        <span class="contact-item">
          <svg class="contact-icon" viewBox="0 0 24 24" aria-hidden="true"><circle cx="12" cy="12" r="12" fill="var(--icon-green)"/><rect x="6" y="8" width="12" height="8.5" rx="1" fill="#fff"/><path d="M6.5 8.6l5.5 4.2 5.5-4.2" stroke="var(--icon-green)" stroke-width="1.3" fill="none"/></svg>
          Bloom@TheHearthsidePlanter.example
        </span>
        <span class="contact-item">
          <svg class="contact-icon" viewBox="0 0 24 24" aria-hidden="true"><circle cx="12" cy="12" r="12" fill="var(--icon-green)"/><circle cx="12" cy="12" r="6" stroke="#fff" stroke-width="1.4" fill="none"/><ellipse cx="12" cy="12" rx="2.6" ry="6" stroke="#fff" stroke-width="1.2" fill="none"/><path d="M6 12h12" stroke="#fff" stroke-width="1.2"/></svg>
          www.TheHearthsidePlanter.example
        </span>
      </div>
    </div>
  </div>
</div>
</body>
</html>
```